依頼詳細
グランドオープンに合わせて4日間限定の来店者プレゼント企画を開催します。その告知として、新聞折り込みにチラシを入れようと思うます。今回はその、折り込み用チラシの作成をお願いいたします。プレゼント内容は5/29,30,31,6/1「プチシュープレゼント」各日50名限定となります。
記載項目
「グランドオープン」であること、「5/29,30、31,6/1各日 50名様限定スイーツプレゼント」があること(プレゼント内容の記載はしても、しなくてもどちらでもokです。)、店名ロゴ(添付)、〒371-0815 群馬県沼田市栄和町2871-5 TEL&FAX 0278-61-7350 SNSページ有♪
サイズ
B5
ページ数
片面
希望イメージ
シンプル 複雑
単色 カラフル
暗い 明るい
日常 高級
遊び心 厳粛
未来的 伝統的
女性的 男性的
希望する色
緑 青
納品ファイル
• 高解像度JPG (.jpg)
補足説明
プレゼント内容の変更。
5/29,30 プチシュー 各日限定50個
5/31,6/1 いちごミルクプリン 各日限定50個 となります。
ロゴファイル追加です

自店のcolorにとてもあっていたから
シンプルなのにインパクトが大きく目を引く配色だったため

色々なデザインを頂きありがとうございました。自分ではなかなか出てこない案が多くロゴの時も感じましたが、とてもいい刺激になりました。
ありがとうございました。

```html
<!DOCTYPE html>
<html lang="ja">
<head>
<meta charset="utf-8">
<title>Sweets&amp;Cafe こもれび グランドオープン</title>
<link rel="stylesheet" href="https://fonts.googleapis.com/css2?family=M+PLUS+Rounded+1c:wght@500;700;800;900&display=swap">
<style>
:root{
  --bg-light:#f4f9d8;
  --bg-mid:#d9ec9a;
  --leaf:#5aa83a;
  --leaf-dark:#2f7d2a;
  --ink:#3b3b3b;
  --pink:#e8457d;
  --orange:#f39a1e;
  --yellow:#f2c81c;
  --blue:#3aa6d8;
  --green:#6dbb3c;
  --purple:#9a5bb8;
  --white:#ffffff;
}
*{margin:0;padding:0;box-sizing:border-box}
html,body{width:855px;height:1200px;overflow:hidden;background:var(--white)}
body{font-family:"M PLUS Rounded 1c",sans-serif;color:var(--ink)}
.flyer{position:relative;width:855px;height:1200px;background:var(--white);overflow:hidden}
.flyer__field{position:absolute;left:22px;top:22px;right:22px;bottom:22px;border-radius:6px;
  background:radial-gradient(ellipse at 50% 40%,var(--bg-light) 0%,#eaf5bf 55%,var(--bg-mid) 100%)}

.brand{position:absolute;left:0;right:0;top:66px;text-align:center}
.brand__sub{font-size:32px;font-weight:800;color:var(--leaf-dark);letter-spacing:1px;line-height:1.2}
.brand__name{display:inline-flex;align-items:center;gap:16px;font-size:84px;font-weight:800;color:var(--leaf-dark);line-height:1.1}
.brand__dot{width:28px;height:28px;border-radius:50%;background:var(--leaf)}
.tagline{position:absolute;left:0;right:0;top:276px;text-align:center;font-size:16px;font-weight:700;color:var(--ink)}

.headline{position:absolute;left:66px;font-weight:900;line-height:1;letter-spacing:2px;font-size:190px;white-space:nowrap}
.headline--grand{top:318px}
.headline--open{top:510px}
.c1{color:var(--pink)}.c2{color:var(--orange)}.c3{color:var(--yellow)}.c4{color:var(--green)}.c5{color:var(--blue)}.c6{color:var(--purple)}
.open-date{position:absolute;left:630px;top:530px;width:190px;color:var(--pink);font-weight:900;text-align:center}
.open-date__num{font-size:80px;line-height:1}
.open-date__day{font-size:40px;margin-top:4px}

.intro{position:absolute;left:57px;top:732px;width:96px;font-size:13px;font-weight:700;line-height:1.55}
.dessert-photo{position:absolute;left:160px;top:732px;width:125px;height:190px;border-radius:4px;
  background:linear-gradient(135deg,#f6d6e1,#f3b0c4 40%,#f7e2a8 75%,#b9dc8a)}

.badge{position:absolute;left:298px;top:738px;width:72px;height:72px;border-radius:50%;background:var(--orange);
  color:var(--white);text-align:center;font-weight:900;display:flex;flex-direction:column;justify-content:center;line-height:1.05}
.badge__big{font-size:28px}.badge__small{font-size:12px}
.gift-title{position:absolute;left:380px;top:738px;font-size:40px;font-weight:900;color:var(--pink);line-height:1.1}
.gift-note{position:absolute;left:392px;top:786px;font-size:14px;font-weight:700;color:var(--ink)}
.gift{position:absolute;top:812px;width:180px;height:108px;border-radius:54px;background:var(--pink);color:var(--white);
  text-align:center;display:flex;flex-direction:column;justify-content:center;font-weight:900}
.gift--choux{left:318px}.gift--pudding{left:515px}
.gift__date{font-size:15px;background:var(--white);color:var(--pink);border-radius:12px;margin:0 20px 6px;padding:2px 0}
.gift__item{font-size:23px;line-height:1.15}

.shop{position:absolute;left:0;right:0;top:945px;text-align:center}
.shop__name{font-size:26px;font-weight:800;color:var(--leaf-dark);line-height:1.3}
.shop__addr{font-size:16px;font-weight:700;line-height:1.5;margin-top:2px}
.shop__tel{font-size:40px;font-weight:900;color:var(--leaf-dark);line-height:1.2;margin-top:2px}
.shop__tel small{font-size:20px;margin-right:8px;color:var(--ink)}

.sns{position:absolute;left:57px;top:1092px;width:240px;height:26px;background:var(--blue);border-radius:4px;
  color:var(--white);font-size:15px;font-weight:800;display:flex;align-items:center;padding-left:10px;gap:8px}
.sns__square{width:14px;height:14px;background:var(--white);border-radius:2px}
.building-photo{position:absolute;left:57px;top:1124px;width:300px;height:50px;
  background:linear-gradient(180deg,#bfe0f2 0%,#dfeef6 45%,#9fbf8a 70%,#6c8a5a 100%)}
.page-preview{position:absolute;left:540px;top:1090px;width:240px;height:84px;border:3px solid var(--white);
  background:linear-gradient(160deg,#e9f4d3,#c6e39a 60%,#f3d2df)}
</style>
</head>
<body>
<main class="flyer">
  <div class="flyer__field" role="img" aria-label="明るい緑の背景に白いクローバー模様"></div>

  <header class="brand">
    <div class="brand__sub">Sweets &amp;Cafe</div>
    <div class="brand__name"><span class="brand__dot"></span>こもれび</div>
  </header>
  <p class="tagline">小さな「ニャッ」が生まれる空間、小さな「ニャッ」を沢山集めて明日への力に・・・。</p>

  <h1>
    <span class="headline headline--grand"><span class="c1">G</span><span class="c2">R</span><span class="c3">A</span><span class="c4">N</span><span class="c5">D</span></span>
    <span class="headline headline--open"><span class="c6">O</span><span class="c1">P</span><span class="c2">E</span><span class="c5">N</span></span>
  </h1>
  <div class="open-date"><div class="open-date__num">5/29</div><div class="open-date__day">木曜日</div></div>

  <p class="intro">香り豊かな20種のお茶、シーズンの果物を使ったシフォンやタルトなど、美味しいケーキ(焼き菓子)を種類豊富な空間で、お楽しみ下さい。</p>
  <div class="dessert-photo" role="img" aria-label="色とりどりのフルーツを使ったスイーツの写真"></div>

  <div class="badge"><span class="badge__big">4</span><span class="badge__small">日間限定</span></div>
  <div class="gift-title">来店者プレゼント</div>
  <div class="gift-note">各日限定50個</div>
  <div class="gift gift--choux"><div class="gift__date">5月29・30日</div><div class="gift__item">プチシュー</div></div>
  <div class="gift gift--pudding"><div class="gift__date">5月31・6月1日</div><div class="gift__item">いちごミルク<br>プリン</div></div>

  <section class="shop">
    <div class="shop__name">Sweets&amp;Cafe こもれび</div>
    <div class="shop__addr">〒371-0815<br>群馬県沼田市栄和町2871-5</div>
    <div class="shop__tel"><small>TEL&amp;FAX</small>0278-61-7350</div>
  </section>

  <div class="sns"><span class="sns__square"></span>SNSページ有♪</div>
  <div class="building-photo" role="img" aria-label="店舗外観の写真"></div>
  <div class="page-preview" role="img" aria-label="店舗SNSページの画面イメージ"></div>
</main>
</body>
</html>
```